Window and GutterCleaning Flyer A5 size double sided.

We need a double sided A5 flyer. Side 1, is for window cleaning, side 2 is for gutter cleaning. Licensed by Borough of Halvern Council.
Phone number 0800 315 4720.
Business address 7 Tarnlow Brae, North Pellin Edinburgh EH14 3RW.
www.clearpane-vista-services.com
We use a LoftPro Gutter inspection Cam to view your gutters first to see if they need doing.
Window cleaning ; Professional window cleaning services, what we offer, water fed pole window cleaning able to reach windows up to 60 feet.
Conservatory cleaning.
Conservatory roof cleaning.
Fascias & Soffits cleaning.
Excellent Customer Service.
Target Market(s)
domestic houses
Industry/Entity Type
window cleaning
Look and feel
Each slider illustrates characteristics of the customer's brand and the style your logo design should communicate.

```html
<!DOCTYPE html>
<html lang="en">
<head>
<meta charset="utf-8">
<title>ClearPane Vista – A5 Flyer, Front and Back</title>
<link rel="stylesheet" href="https://fonts.googleapis.com/css2?family=Poppins:wght@500;600;700;800&display=swap">
<style>
  :root{
    --navy:#27285e;
    --sky:#a9cbf0;
    --sky-soft:#c4dbf5;
    --lavender:#e1e4f4;
    --stage:#f1f2f6;
    --white:#ffffff;
  }
  *{box-sizing:border-box;margin:0;padding:0}
  html,body{width:1200px;height:800px;overflow:hidden}
  body{background:var(--stage);font-family:"Poppins",Arial,sans-serif;color:var(--navy);position:relative}

  .flyer{position:absolute;top:50px;width:495px;height:700px;overflow:hidden;background:var(--lavender);box-shadow:0 10px 30px rgba(39,40,94,.18)}
  .flyer--front{left:75px}
  .flyer--back{left:630px}
  .abs{position:absolute}

  /* brand badge */
  .brand-badge{position:absolute;top:-70px;right:-55px;width:215px;height:215px;border-radius:50%;background:var(--sky);border:3px solid var(--navy)}
  .brand-name{position:absolute;top:28px;right:14px;width:120px;text-align:center;font-weight:700;font-size:17px;line-height:1.15;color:var(--navy)}

  /* image placeholders */
  .ph{position:absolute}
  .ph--rounded{border-radius:12px;border:3px solid var(--white)}

  .wave{position:absolute;left:0;width:100%}

  /* front copy */
  .intro{left:24px;top:388px;width:305px;font-weight:700;font-size:12px;line-height:1.25}
  .offer-title{left:24px;top:452px;font-weight:800;font-size:15px;line-height:1.3}
  .offer-list{left:24px;top:475px;width:310px;list-style:none;font-weight:500;font-size:12px;line-height:1.18}
  .offer-list li{position:relative;padding-left:16px;margin-bottom:1px}
  .offer-list li::before{content:"";position:absolute;left:2px;top:5px;width:6px;height:6px;border-radius:50%;background:var(--navy)}

  .phone-band{left:0;top:598px;width:335px;height:46px;background:var(--sky);border-radius:0 12px 0 0;display:flex;align-items:center;gap:10px;padding-left:16px}
  .phone-number{font-weight:800;font-size:33px;letter-spacing:.5px;color:var(--navy);white-space:nowrap;line-height:1.1}

  .address{background:var(--navy);color:var(--sky-soft);display:flex;align-items:flex-start;gap:8px;font-weight:500;font-size:12px;line-height:1.3;padding:12px 14px}
  .web{background:var(--sky);display:flex;align-items:center;gap:7px;font-weight:500;font-size:11px;padding:0 12px;white-space:nowrap}

  /* back copy */
  .cam-band{left:95px;top:372px;width:400px;height:80px;background:var(--sky);display:flex;align-items:center;justify-content:center;text-align:center;font-weight:700;font-size:15px;line-height:1.2;padding:0 18px}
  .service-list{left:170px;top:470px;list-style:none;font-weight:600;font-size:16px;line-height:1.35}
  .service-list li{position:relative;padding-left:16px}
  .service-list li::before{content:"";position:absolute;left:1px;top:9px;width:7px;height:7px;border-radius:50%;background:var(--navy)}
  .licence{font-weight:500;font-size:11px;color:var(--sky-soft);margin-top:3px}
</style>
</head>
<body>

<!-- FRONT: window cleaning -->
<section class="flyer flyer--front" aria-label="Flyer front – window cleaning">
  <div class="ph" style="left:0;top:0;width:125px;height:380px;background:linear-gradient(160deg,#9fb4cf,#c7d3e3 50%,#8fa3bf)" role="img" aria-label="Close-up of a water-fed pole brush spraying water on glass"></div>
  <div class="ph" style="left:125px;top:0;width:180px;height:380px;background:linear-gradient(180deg,#a9b6c4 0%,#8a4b3a 30%,#7c4436 70%,#c8b98e 100%);border-left:3px solid var(--white)" role="img" aria-label="Red-brick house with white windows and balcony"></div>
  <div class="ph" style="left:305px;top:0;width:190px;height:380px;background:linear-gradient(170deg,#6f7b88,#d8dde3 40%,#aeb7c1);border-left:3px solid var(--white)" role="img" aria-label="Window frame being cleaned with a pole brush"></div>

  <div class="brand-badge"></div>
  <div class="brand-name">ClearPane Vista</div>

  <svg class="wave" style="top:295px" width="495" height="110" viewBox="0 0 495 110" aria-hidden="true">
    <path d="M0 95 C140 40 300 20 495 30 L495 110 L0 110 Z" fill="var(--lavender)"/>
    <path d="M0 80 C140 30 300 10 495 18 L495 30 C300 22 140 42 0 95 Z" fill="var(--navy)"/>
  </svg>

  <div class="ph ph--rounded" style="left:337px;top:322px;width:146px;height:96px;background:linear-gradient(150deg,#d7dde6,#5a6c80)" role="img" aria-label="Squeegee cleaning a window"></div>
  <div class="ph ph--rounded" style="left:337px;top:428px;width:146px;height:96px;background:linear-gradient(180deg,#e8ecf2,#b7a391)" role="img" aria-label="White conservatory"></div>
  <div class="ph ph--rounded" style="left:337px;top:534px;width:146px;height:96px;background:linear-gradient(150deg,#bfd8ee,#7ea6cf)" role="img" aria-label="Hand spraying cleaner on glass"></div>

  <p class="abs intro">Serving the West Edinburgh area with over 30 years of experience, we've earned reputation for trusted, high-quality service – and we take pride in every window we clean.</p>
  <h2 class="abs offer-title">We Offer:</h2>
  <ul class="abs offer-list">
    <li>Regular domestic &amp; commercial window cleaning</li>
    <li>Water-fed pole system – reach up to 60 feet safely from the ground</li>
    <li>Frame, sill &amp; door cleans included as standard</li>
    <li>One-off &amp; contract services available</li>
    <li>Eco-friendly pure water system – no chemicals, no residue</li>
  </ul>

  <div class="abs phone-band">
    <svg width="26" height="26" viewBox="0 0 24 24" aria-hidden="true"><path fill="var(--navy)" d="M6.6 10.8a15.1 15.1 0 0 0 6.6 6.6l2.2-2.2a1 1 0 0 1 1-.25 11.4 11.4 0 0 0 3.6.57 1 1 0 0 1 1 1V20a1 1 0 0 1-1 1A17 17 0 0 1 3 4a1 1 0 0 1 1-1h3.5a1 1 0 0 1 1 1c0 1.25.2 2.45.57 3.57a1 1 0 0 1-.25 1z"/></svg>
    <span class="phone-number">0800 315 4720</span>
  </div>

  <div class="abs address" style="left:0;top:644px;width:270px;height:56px">
    <svg width="14" height="20" viewBox="0 0 14 20" aria-hidden="true"><path fill="var(--sky-soft)" d="M7 0a7 7 0 0 0-7 7c0 5 7 13 7 13s7-8 7-13a7 7 0 0 0-7-7zm0 9.5A2.5 2.5 0 1 1 7 4.5a2.5 2.5 0 0 1 0 5z"/></svg>
    <span>7 Tarnlow Brae,<br>North Pellin Edinburgh EH14 3RW</span>
  </div>
  <div class="abs web" style="left:270px;top:644px;width:225px;height:56px;font-size:10.5px">
    <svg width="15" height="15" viewBox="0 0 20 20" aria-hidden="true"><g fill="none" stroke="var(--navy)" stroke-width="1.8"><circle cx="10" cy="10" r="8.5"/><ellipse cx="10" cy="10" rx="3.8" ry="8.5"/><path d="M1.5 10h17"/></g></svg>
    <span>www.clearpane-vista-services.com</span>
  </div>
</section>

<!-- BACK: gutter cleaning -->
<section class="flyer flyer--back" aria-label="Flyer back – gutter cleaning">
  <div class="ph" style="left:0;top:0;width:495px;height:380px;background:linear-gradient(160deg,#4f5660 0%,#8a6a4a 40%,#a97c4f 60%,#7f8d5a 100%)" role="img" aria-label="Gloved hands clearing leaves from a gutter"></div>
  <div class="ph" style="left:125px;top:230px;width:175px;height:140px;border-radius:14px;background:linear-gradient(180deg,#2c2f35,#5b6f85)" role="img" aria-label="Gutter inspection camera monitor"></div>

  <div class="brand-badge"></div>
  <div class="brand-name">ClearPane Vista</div>

  <div class="ph" style="left:0;top:440px;width:495px;height:260px;background:linear-gradient(180deg,#d9dceb,#e4e5ef 60%,#cfd3e6)" role="img" aria-label="Faded background of autumn leaves"></div>

  <svg class="wave" style="top:320px" width="495" height="70" viewBox="0 0 495 70" aria-hidden="true">
    <path d="M0 30 C150 58 330 52 495 20 L495 70 L0 70 Z" fill="var(--lavender)"/>
    <path d="M0 18 C150 46 330 40 495 8 L495 20 C330 52 150 58 0 30 Z" fill="var(--navy)"/>
  </svg>

  <div class="abs cam-band">We use a LoftPro Gutter inspection Cam to view your gutters first to see if they need doing</div>

  <div class="ph ph--rounded" style="left:18px;top:460px;width:138px;height:78px;background:linear-gradient(160deg,#5d6570,#9aa3ad)" role="img" aria-label="Cleaning a roofline gutter"></div>
  <div class="ph ph--rounded" style="left:18px;top:546px;width:138px;height:80px;background:linear-gradient(180deg,#6e4a36,#c9c4bd)" role="img" aria-label="Conservatory roof interior"></div>

  <div class="ph" style="left:330px;top:480px;width:165px;height:220px;background:linear-gradient(200deg,#e9e3dc,#c9b39c 55%,#dfe2ee)" role="img" aria-label="Smiling customer service adviser wearing a headset"></div>

  <ul class="abs service-list">
    <li>Conservatory cleaning.</li>
    <li>Conservatory roof cleaning.</li>
    <li>Fascias &amp; Soffits cleaning.</li>
    <li>Excellent Customer Service.</li>
  </ul>

  <div class="abs phone-number" style="left:170px;top:586px">0800 315 4720</div>

  <div class="abs address" style="left:0;top:632px;width:250px;height:68px;flex-direction:column;gap:0;padding:8px 12px">
    <div style="display:flex;gap:8px">
      <svg width="13" height="18" viewBox="0 0 14 20" aria-hidden="true"><path fill="var(--sky-soft)" d="M7 0a7 7 0 0 0-7 7c0 5 7 13 7 13s7-8 7-13a7 7 0 0 0-7-7zm0 9.5A2.5 2.5 0 1 1 7 4.5a2.5 2.5 0 0 1 0 5z"/></svg>
      <span style="font-size:11px">7 Tarnlow Brae,<br>North Pellin Edinburgh EH14 3RW</span>
    </div>
    <div class="licence">Licensed by Borough of Halvern Council</div>
  </div>
  <div class="abs web" style="left:250px;top:670px;width:245px;height:30px">
    <svg width="15" height="15" viewBox="0 0 20 20" aria-hidden="true"><g fill="none" stroke="var(--navy)" stroke-width="1.8"><circle cx="10" cy="10" r="8.5"/><ellipse cx="10" cy="10" rx="3.8" ry="8.5"/><path d="M1.5 10h17"/></g></svg>
    <span>www.clearpane-vista-services.com</span>
  </div>
</section>

</body>
</html>
```